Business Card Design Project

I am a Chiropractor that is looking for a new business card.  Our logo was slightly changed lately, therefore need a new, more professional look.
We are a modern, non-stuffy chiropractic office.  Want a contemporary look that will let people know this is not your typical doctors office.  Our logo is red, and contains the name of our business: realign.  The u in the logo is green, stressing the most important part of our business: "u"

Target Market(s)
moderate to upper income bracket, family friendly
www.realignspine-example.com
Gordon Pell
Family Chiropractor
314 Hollis Rd
Ferncliff, OR 97999
555.555.0147 phone
555.555.0148 fax
Industry/Entity Type
Business
Requirements
Must have
- www.realignspine-example.com
Gordon Pell
Family Chiropractor
314 Hollis Rd
Ferncliff, OR 97999
555.555.0147 phone
555.555.0148 fax

```html
<!DOCTYPE html>
<html lang="en">
<head>
<meta charset="utf-8">
<title>realign – Business Card</title>
<link rel="stylesheet" href="https://fonts.googleapis.com/css2?family=Open+Sans:ital,wght@0,400;0,600;1,400&display=swap">
<style>
  :root {
    --page-bg: #d9d4cc;
    --card-black: #050505;
    --card-charcoal: #2a2a2a;
    --band-top: #4a4847;
    --band-bottom: #3a3938;
    --band-rule: #8d8a86;
    --text-light: #d6cfc4;
    --text-muted: #a9a49c;
    --text-web: #8e7476;
    --brand-red: #d2322d;
  }
  * { box-sizing: border-box; margin: 0; padding: 0; }
  html, body {
    width: 1200px; height: 970px; overflow: hidden;
    background: var(--page-bg);
    font-family: "Open Sans", Arial, sans-serif;
  }
  .card {
    position: absolute; left: 120px; top: 218px;
    width: 960px; height: 533px;
    background:
      radial-gradient(ellipse 45% 70% at 30% 60%, rgba(70,70,70,.55), transparent 70%),
      linear-gradient(100deg, var(--card-charcoal) 0%, var(--card-black) 55%, #111 100%);
    overflow: hidden;
    box-shadow: 0 10px 30px rgba(0,0,0,.25);
  }
  .card__band {
    position: absolute; left: 0; top: 0; right: 0; height: 135px;
    background: linear-gradient(180deg, var(--band-top), var(--band-bottom));
    border-bottom: 1px solid var(--band-rule);
  }
  .brand {
    position: absolute; right: 48px; top: 66px;
    display: flex; align-items: center; gap: 12px;
  }
  .brand__dot {
    width: 20px; height: 20px; border-radius: 50%;
    background: var(--brand-red);
  }
  .brand__name {
    font-size: 44px; font-weight: 400; letter-spacing: 1px;
    color: var(--text-light); line-height: 1;
  }
  .contact {
    position: absolute; left: 46px; top: 250px;
    color: var(--text-light);
  }
  .contact__name { font-size: 22px; font-weight: 600; line-height: 1.2; }
  .contact__title { font-size: 18px; font-style: italic; color: var(--text-muted); margin-top: 2px; }
  .contact__details {
    margin-top: 22px; font-size: 17.5px; font-weight: 600; line-height: 26px;
    list-style: none;
  }
  .contact__web {
    margin-top: 30px; font-size: 21px; font-weight: 600; color: var(--text-web);
  }
</style>
</head>
<body>
  <div class="card">
    <div class="card__band"></div>
    <div class="brand">
      <span class="brand__dot"></span>
      <span class="brand__name">realign</span>
    </div>
    <div class="contact">
      <p class="contact__name">Gordon Pell</p>
      <p class="contact__title">Family Chiropractor</p>
      <ul class="contact__details">
        <li>314 Hollis Rd</li>
        <li>Ferncliff, OR 97999</li>
        <li>555.555.0147 phone</li>
        <li>555.555.0148 fax</li>
      </ul>
      <p class="contact__web">www.realignspine-example.com</p>
    </div>
  </div>
</body>
</html>
```